Packaging Tape Design for Retail / Ecommerce Company

We need a design for custom packing tape for our company. We would like to see two designs for the packaging tape. 1) with the word fragile attached 2) Similiar design without the fragileMinimum resolution is 300 .ppi 3" x 6" or 3" x 12" - If selected, request that font that are used be identified. Orla Hearth Logo and package - Nest Bright! is a tagline we use on documents and correspondence. Looking for a creative design.

Target Market(s)

Mid level to high end consumers

Industry/Entity Type

Retail

Font styles to use
Sans Serif

Requirements
Must have
• logo must be included
• Nest Bright! - must be included
• web address: orlahearth.com
Nice to have
• creativity

```html
<!DOCTYPE html>
<html lang="en">
<head>
<meta charset="utf-8">
<title>Orla Hearth Packaging Tape</title>
<link rel="stylesheet" href="https://fonts.googleapis.com/css2?family=Kaushan+Script&family=Open+Sans:wght@400;700&display=swap">
<style>
  :root {
    --brick: #7d1a0e;
    --cream: #efeacb;
    --cream-edge: #d9d2ab;
    --ink-dark: #3b2a26;
    --backdrop: #ecebe8;
  }
  * { margin: 0; padding: 0; box-sizing: border-box; }
  html, body { width: 1200px; height: 733px; overflow: hidden; }
  body {
    background: var(--backdrop);
    font-family: "Open Sans", Arial, sans-serif;
    position: relative;
  }
  .brand-lockup {
    position: absolute;
    top: 48px;
    right: 110px;
    width: 260px;
    text-align: center;
  }
  .brand-panel {
    background: var(--cream);
    border-radius: 10px;
    padding: 28px 10px;
    display: flex;
    align-items: center;
    justify-content: center;
    gap: 10px;
  }
  .brand-mark {
    width: 14px; height: 14px;
    border-radius: 50%;
    background: var(--brick);
  }
  .brand-name {
    font-weight: 700;
    font-size: 32px;
    color: var(--brick);
    letter-spacing: 1px;
  }
  .brand-tagline {
    font-family: "Kaushan Script", cursive;
    font-size: 34px;
    color: var(--brick);
    margin-top: 26px;
    line-height: 1;
  }
  .brand-url {
    font-size: 20px;
    letter-spacing: 2px;
    color: var(--ink-dark);
    margin-top: 4px;
  }
  .tape {
    position: absolute;
    left: 0;
    width: 1200px;
    height: 170px;
    display: flex;
    overflow: hidden;
  }
  .tape--brick { top: 270px; background: var(--brick); }
  .tape--cream { top: 500px; background: var(--cream); border-top: 1px solid var(--cream-edge); border-bottom: 1px solid var(--cream-edge); }
  .tape-unit {
    flex: 0 0 300px;
    display: flex;
    flex-direction: column;
    justify-content: space-between;
    padding: 12px 18px;
  }
  .tape-unit--flip { flex-direction: column-reverse; }
  .tape-panel {
    height: 88px;
    border-radius: 8px;
    display: flex;
    align-items: center;
    justify-content: center;
    gap: 8px;
  }
  .tape--brick .tape-panel { background: var(--cream); }
  .tape--cream .tape-panel { background: var(--cream); border: 2px solid var(--brick); }
  .tape-panel .brand-mark { width: 10px; height: 10px; }
  .tape-panel .brand-name { font-size: 26px; }
  .tape-copy { line-height: 1.05; padding-left: 6px; }
  .tape-tagline { font-family: "Kaushan Script", cursive; font-size: 24px; }
  .tape-url { font-size: 15px; letter-spacing: 1.5px; }
  .tape--brick .tape-copy { color: var(--cream); }
  .tape--cream .tape-tagline { color: var(--brick); }
  .tape--cream .tape-url { color: var(--ink-dark); }
</style>
</head>
<body>

<section class="brand-lockup">
  <div class="brand-panel"><span class="brand-mark"></span><span class="brand-name">Orla Hearth</span></div>
  <p class="brand-tagline">Nest Bright!</p>
  <p class="brand-url">orlahearth.com</p>
</section>

<section class="tape tape--brick">
  <div class="tape-unit"><div class="tape-panel"><span class="brand-mark"></span><span class="brand-name">Orla Hearth</span></div><div class="tape-copy"><p class="tape-tagline">Nest Bright!</p><p class="tape-url">orlahearth.com</p></div></div>
  <div class="tape-unit tape-unit--flip"><div class="tape-panel"><span class="brand-mark"></span><span class="brand-name">Orla Hearth</span></div><div class="tape-copy"><p class="tape-tagline">Nest Bright!</p><p class="tape-url">orlahearth.com</p></div></div>
  <div class="tape-unit"><div class="tape-panel"><span class="brand-mark"></span><span class="brand-name">Orla Hearth</span></div><div class="tape-copy"><p class="tape-tagline">Nest Bright!</p><p class="tape-url">orlahearth.com</p></div></div>
  <div class="tape-unit tape-unit--flip"><div class="tape-panel"><span class="brand-mark"></span><span class="brand-name">Orla Hearth</span></div><div class="tape-copy"><p class="tape-tagline">Nest Bright!</p><p class="tape-url">orlahearth.com</p></div></div>
</section>

<section class="tape tape--cream">
  <div class="tape-unit tape-unit--flip"><div class="tape-panel"><span class="brand-mark"></span><span class="brand-name">Orla Hearth</span></div><div class="tape-copy"><p class="tape-tagline">Nest Bright!</p><p class="tape-url">orlahearth.com</p></div></div>
  <div class="tape-unit"><div class="tape-panel"><span class="brand-mark"></span><span class="brand-name">Orla Hearth</span></div><div class="tape-copy"><p class="tape-tagline">Nest Bright!</p><p class="tape-url">orlahearth.com</p></div></div>
  <div class="tape-unit tape-unit--flip"><div class="tape-panel"><span class="brand-mark"></span><span class="brand-name">Orla Hearth</span></div><div class="tape-copy"><p class="tape-tagline">Nest Bright!</p><p class="tape-url">orlahearth.com</p></div></div>
  <div class="tape-unit"><div class="tape-panel"><span class="brand-mark"></span><span class="brand-name">Orla Hearth</span></div><div class="tape-copy"><p class="tape-tagline">Nest Bright!</p><p class="tape-url">orlahearth.com</p></div></div>
</section>

</body>
</html>
```